Postcard Design

I would like to make a post card that announces a new aspect of my business: Selling NEW pianos along with recondition instruments. Here is aYouTube video that should be helpful in understanding what I am up to: http://vidlorn.example/qwtPzrmaBn4

Here is my website for more information about my business:
http://www.keytonetuneworks.example/ There you will find on the front page a link to my Facebook business page where there are other information and photos.

I have offered reconditioned pianos for rent and sale for the last few years, but this year I am selling new piano from Dorvel and Brekta - logos for them are below.

I am wanting something professional, but exciting/splashy. Use the business logo of the car too.
Updates

Project Deadline Extended
Reason: I was out of town and didn't have time to consider these unitl now. I would like to see what you might do in response to what I have sent over the next day or two. Thank you!!!

Target Market(s)

Piano Clients and prospective clients

Industry/Entity Type

Business

```html
<!DOCTYPE html>
<html lang="en">
<head>
<meta charset="utf-8">
<title>Keytone Tuneworks – Postcard</title>
<link rel="stylesheet" href="https://fonts.googleapis.com/css2?family=Great+Vibes&family=Pinyon+Script&family=Cinzel:wght@400;600&display=swap">
<style>
  :root {
    --page-bg: #d9d6d3;
    --card-bg: #221d20;
    --accent-red: #a3202a;
    --brand-pink: #c8185a;
    --title-pink: #f1d9df;
    --text-light: #ece8e6;
    --photo-light: #d8d8d8;
    --photo-dark: #3a3a3a;
  }
  * { margin: 0; padding: 0; box-sizing: border-box; }
  html, body {
    width: 1200px;
    height: 1069px;
    overflow: hidden;
    background: var(--page-bg);
  }
  .stage {
    width: 1200px;
    height: 1069px;
    display: flex;
    align-items: center;
    justify-content: center;
  }
  .postcard {
    position: relative;
    width: 1000px;
    height: 560px;
    background: var(--card-bg);
    overflow: hidden;
    box-shadow: 0 18px 40px rgba(0, 0, 0, 0.35);
  }
  .photo-band {
    position: absolute;
    inset: 0;
    width: 1000px;
    height: 560px;
  }
  .announcement {
    position: absolute;
    left: 34px;
    top: 22px;
    font-family: "Great Vibes", cursive;
    font-size: 30px;
    color: var(--text-light);
    white-space: nowrap;
  }
  .brand-row {
    position: absolute;
    left: 180px;
    top: 92px;
    display: flex;
    align-items: center;
    gap: 26px;
    font-family: "Cinzel", serif;
    font-weight: 600;
    color: var(--text-light);
  }
  .brand {
    display: flex;
    align-items: center;
    gap: 10px;
    font-size: 26px;
    letter-spacing: 1px;
  }
  .brand-mark {
    width: 14px;
    height: 14px;
    background: var(--brand-pink);
  }
  .brand-mark.round {
    border-radius: 50%;
    background: var(--text-light);
  }
  .business-name {
    position: absolute;
    right: 60px;
    top: 338px;
    font-family: "Pinyon Script", cursive;
    font-size: 64px;
    font-weight: 400;
    color: var(--title-pink);
    white-space: nowrap;
  }
  .tagline {
    position: absolute;
    right: 60px;
    top: 470px;
    font-family: "Cinzel", serif;
    font-size: 17px;
    letter-spacing: 5px;
    color: var(--text-light);
    white-space: nowrap;
  }
  .tagline .gap { display: inline-block; width: 22px; }
</style>
</head>
<body>
  <main class="stage">
    <section class="postcard">
      <svg class="photo-band" viewBox="0 0 1000 560">
        <defs>
          <linearGradient id="photoTone" x1="0" y1="0" x2="1" y2="1">
            <stop offset="0" stop-color="#d8d8d8"/>
            <stop offset="0.55" stop-color="#9a9a9a"/>
            <stop offset="1" stop-color="#3a3a3a"/>
          </linearGradient>
        </defs>
        <polygon points="0,250 1000,30 1000,140 0,430" fill="url(#photoTone)"
                 role="img" aria-label="Black and white photograph of a pianist playing a grand piano in a bright room"/>
        <line x1="0" y1="250" x2="1000" y2="30" stroke="#a3202a" stroke-width="4"/>
        <line x1="0" y1="430" x2="1000" y2="140" stroke="#a3202a" stroke-width="4"/>
      </svg>

      <p class="announcement">Guess who is now selling NEW pianos at a substantial savings from his shop!</p>

      <div class="brand-row">
        <span class="brand"><span class="brand-mark"></span>Dorvel</span>
        <span class="brand"><span class="brand-mark round"></span>Brekta</span>
      </div>

      <h1 class="business-name">Keytone Tuneworks</h1>
      <p class="tagline">RECONDITIONED PIANOS<span class="gap"></span>AVAILABLE FOR SALE AND RENT</p>
    </section>
  </main>
</body>
</html>
```